Design an Outstanding flyer for my company.

I need a flyer designed for our window tinting company based in Brisbane Queensland Australia. The flyer will be targeting Home tinting. We also do mobile car tinting. Something in regards to this could be incorporated into the flyer as well.
I want it to be 2 sided DL size. Black background.
It really needs to Pop, and be a real attention getter.
It needs to be easy to read.
I have provided a mock up with the info on it from our marketing company. It will need a spellcheck etc to make sure everything is correct.
Everything about it can be changed however you like.
I have also included the company logo.

Lets see what you've got!

Target Market(s)

Home Owners

Industry/Entity Type

Home Improvement

Font styles to use
Other font styles liked:
• Duan Penh

Requirements
Must have
• All the information on the mock up. Clear and easy to read.
• Must Stand Out!

```html
<!DOCTYPE html>
<html lang="en">
<head>
<meta charset="utf-8">
<title>BrightPeak Window Tinting – DL Flyer</title>
<link href="https://fonts.googleapis.com/css2?family=Anton&family=Oswald:wght@500&family=Montserrat:wght@400;500;600&display=swap" rel="stylesheet">
<style>
  :root{
    --stage:#d9dde2;
    --ink:#0d0d0d;
    --panel:#151515;
    --panel-hi:#2a2a2a;
    --silver:#c9c9c9;
    --gold:#ffd21a;
    --gold-deep:#f39a00;
    --orange:#ff9a00;
    --red:#ff2a2a;
    --purple:#7a2cff;
    --white:#ffffff;
    --grey-text:#e6e6e6;
  }
  *{box-sizing:border-box;margin:0;padding:0}
  html,body{width:1200px;height:1200px;overflow:hidden}
  body{background:var(--stage);display:flex;justify-content:center;align-items:center;gap:58px;font-family:"Montserrat",sans-serif}

  .flyer{position:relative;width:468px;height:992px;background:linear-gradient(180deg,#1b1b1b 0%,var(--ink) 14%,#111 100%);color:var(--white);overflow:hidden;display:flex;flex-direction:column;align-items:center;box-shadow:0 10px 30px rgba(0,0,0,.35)}

  .brand{height:132px;width:100%;display:flex;align-items:center;justify-content:center;gap:14px;background:linear-gradient(180deg,#2c2c2c 0%,#0a0a0a 100%)}
  .brand-dot{width:40px;height:40px;border-radius:50%;background:var(--gold)}
  .brand-name{font-family:"Montserrat",sans-serif;font-weight:600;color:var(--gold);font-size:24px;letter-spacing:1px;line-height:1.15;text-transform:uppercase}
  .brand-name small{display:block;font-size:9.5px;letter-spacing:7px;font-weight:600}

  .divider{width:100%;height:38px;display:block;flex:none}

  .hero{display:flex;flex-direction:column;align-items:center;text-align:center}
  .tagline-top{font-family:"Montserrat",sans-serif;font-weight:600;font-size:15.5px;line-height:1.25;color:var(--grey-text);margin:6px 0 6px}
  .keep{font-family:"Anton",sans-serif;font-size:58px;line-height:1.05;background:linear-gradient(90deg,var(--gold) 0%,var(--gold) 60%,var(--gold-deep) 100%);-webkit-background-clip:text;background-clip:text;color:transparent}
  .claims{display:flex;align-items:center;gap:14px;font-family:"Anton",sans-serif;margin-top:2px}
  .uv{display:flex;align-items:center;gap:6px}
  .uv-label{font-size:20px;line-height:.95;text-align:left}
  .uv-label span{display:block;font-size:14px}
  .uv-num{font-size:44px;line-height:1}
  .uv-num sup{font-size:20px;vertical-align:top}
  .sep{width:2px;height:40px;background:var(--white)}
  .private{text-align:left;line-height:1}
  .private span{display:block;font-size:17px;letter-spacing:5px}
  .private b{font-weight:400;font-size:32px}
  .save{font-family:"Anton",sans-serif;font-size:58px;line-height:1.1;background:linear-gradient(90deg,var(--red) 0%,#e5247a 45%,var(--purple) 100%);-webkit-background-clip:text;background-clip:text;color:transparent}

  .benefits{position:relative;width:100%;padding:22px 40px 20px 52px}
  .benefits-bg{position:absolute;inset:0;z-index:0}
  .benefit-list{position:relative;z-index:1;display:grid;grid-template-columns:193px 1fr;column-gap:0;list-style:none}
  .benefit-col{display:flex;flex-direction:column;gap:9px}
  .benefit{font-family:"Oswald",sans-serif;font-weight:500;font-size:12.5px;line-height:1.33;text-transform:uppercase;padding-left:17px;position:relative;list-style:none;color:var(--grey-text)}
  .benefit::before{content:"";position:absolute;left:0;top:4px;width:10px;height:10px;border-radius:50%;background:radial-gradient(circle at 35% 35%,#ffd27a,var(--orange) 60%)}

  .contact{display:flex;flex-direction:column;align-items:center;text-align:center;width:100%}
  .reasons{font-family:"Montserrat",sans-serif;font-weight:600;font-size:15px;line-height:1.05;margin-top:8px}
  .cta{font-family:"Anton",sans-serif;color:var(--gold);font-size:27px;line-height:1.02;margin-top:14px;padding-bottom:6px;border-bottom:1px solid #555;letter-spacing:.5px}
  .phones{display:grid;grid-template-columns:62px auto;align-items:center;row-gap:6px;margin-top:10px}
  .phone-icon{width:36px;height:36px;justify-self:center}
  .sms{font-family:"Montserrat",sans-serif;color:var(--gold);font-size:20px;justify-self:center}
  .num{font-family:"Anton",sans-serif;font-size:44px;line-height:1.05;letter-spacing:1.5px;text-align:left}
  .web{font-size:13px;font-weight:500;margin-top:12px}
</style>
</head>
<body>

<!-- FRONT -->
<article class="flyer flyer--front">
  <header class="brand"><span class="brand-dot"></span><div class="brand-name">BrightPeak<small>Window Tinting</small></div></header>
  <svg class="divider" viewBox="0 0 468 38" preserveAspectRatio="none"><path d="M0 4 H60 Q80 4 95 20 Q108 34 130 34 H338 Q360 34 373 20 Q388 4 408 4 H468" fill="none" stroke="var(--silver)" stroke-width="4"/></svg>
  <section class="hero">
    <div class="keep">KEEP HEAT OUT</div>
    <div class="claims">
      <div class="uv"><div class="uv-label">BLOCK<span>UV RAYS</span></div><div class="uv-num">99.9<sup>%</sup></div></div>
      <div class="sep"></div>
      <div class="private"><span>INCREASE</span><b>PRIVATE</b></div>
    </div>
    <div class="save">SAVE MONEY</div>
  </section>
  <svg class="divider" viewBox="0 0 468 38" preserveAspectRatio="none" style="margin-top:14px"><path d="M0 34 H60 Q80 34 95 18 Q108 4 130 4 H338 Q360 4 373 18 Q388 34 408 34 H468" fill="none" stroke="var(--silver)" stroke-width="4"/></svg>
  <section class="benefits">
    <div class="benefits-bg" role="img" aria-label="Car interior photograph behind the benefit list" style="background:radial-gradient(ellipse at 50% 55%,#3a3a3a 0%,#1a1a1a 55%,#0c0c0c 100%)"></div>
    <ul class="benefit-list">
      <li class="benefit-col"><ul>
        <li class="benefit">Reduce glare</li>
        <li class="benefit">Reduce energy costs</li>
        <li class="benefit">Control the amount of<br>light entering your home</li>
        <li class="benefit">Reduce carbon footprint</li>
        <li class="benefit">Make home more beautiful</li>
        <li class="benefit">Eliminate home hot spots.</li>
        <li class="benefit">Protect against broken glass</li>
        <li class="benefit">Regulate energy</li>
      </ul></li>
      <li class="benefit-col"><ul>
        <li class="benefit">Protects upholstery</li>
        <li class="benefit">Improve effectiveness<br>of roof insulation</li>
        <li class="benefit">Improve health</li>
        <li class="benefit">Reduces interior floor fading</li>
        <li class="benefit">Eliminate need for blinds</li>
        <li class="benefit">Strengthen your windows</li>
        <li class="benefit">Insulate in winter</li>
        <li class="benefit">Affoardable</li>
      </ul></li>
    </ul>
  </section>
  <svg class="divider" viewBox="0 0 468 38" preserveAspectRatio="none"><path d="M0 4 H60 Q80 4 95 20 Q108 34 130 34 H338 Q360 34 373 20 Q388 4 408 4 H468" fill="none" stroke="var(--silver)" stroke-width="4"/></svg>
  <section class="contact">
    <p class="reasons">20 REASONS WHY HOME WINDOW TINTING<br>IS PERFECT FOR YOU</p>
    <p class="cta">CALL BRISBANE’S LEADER IN<br>HOME WINDOW TINTING NOW</p>
    <div class="phones">
      <svg class="phone-icon" viewBox="0 0 36 36"><circle cx="18" cy="18" r="16" fill="none" stroke="var(--gold)" stroke-width="2.5"/><path d="M12 9 l4 0 l1.5 5 l-2.5 2 q2 4 6 6 l2 -2.5 l5 1.5 l0 4 q-1 2 -4 2 q-8 -1 -13 -9 q-2 -5 1 -9z" fill="var(--gold)"/></svg>
      <span class="num">07 3100 4820</span>
      <span class="sms">SMS</span>
      <span class="num">0400 512 736</span>
    </div>
    <p class="web">www.brightpeaktinting.com.au</p>
  </section>
</article>

<!-- BACK -->
<article class="flyer flyer--back">
  <header class="brand"><span class="brand-dot"></span><div class="brand-name">BrightPeak<small>Window Tinting</small></div></header>
  <svg class="divider" viewBox="0 0 468 38" preserveAspectRatio="none"><path d="M0 4 H60 Q80 4 95 20 Q108 34 130 34 H338 Q360 34 373 20 Q388 4 408 4 H468" fill="none" stroke="var(--silver)" stroke-width="4"/></svg>
  <section class="hero">
    <p class="tagline-top">20 REASONS WHY HOME WINDOW TINTING<br>IS PERFECT FOR YOU</p>
    <div class="keep">KEEP HEAT OUT</div>
    <div class="claims">
      <div class="uv"><div class="uv-label">BLOCK<span>UV RAYS</span></div><div class="uv-num">99.9<sup>%</sup></div></div>
      <div class="sep"></div>
      <div class="private"><span>INCREASE</span><b>PRIVATE</b></div>
    </div>
    <div class="save">SAVE MONEY</div>
  </section>
  <svg class="divider" viewBox="0 0 468 38" preserveAspectRatio="none" style="margin-top:10px"><path d="M0 34 H60 Q80 34 95 18 Q108 4 130 4 H338 Q360 4 373 18 Q388 34 408 34 H468" fill="none" stroke="var(--silver)" stroke-width="4"/></svg>
  <section class="benefits">
    <div class="benefits-bg" role="img" aria-label="Modern home exterior at dusk behind the benefit list" style="background:linear-gradient(180deg,#262626 0%,#3b3b3b 45%,#141414 100%)"></div>
    <ul class="benefit-list">
      <li class="benefit-col"><ul>
        <li class="benefit">Reduce glare</li>
        <li class="benefit">Reduce energy costs</li>
        <li class="benefit">Control the amount of<br>light entering your home</li>
        <li class="benefit">Reduce carbon footprint</li>
        <li class="benefit">Make home more beautiful</li>
        <li class="benefit">Eliminate home hot spots.</li>
        <li class="benefit">Protect against broken glass</li>
        <li class="benefit">Regulate energy</li>
      </ul></li>
      <li class="benefit-col"><ul>
        <li class="benefit">Protects upholstery</li>
        <li class="benefit">Improve effectiveness<br>of roof insulation</li>
        <li class="benefit">Improve health</li>
        <li class="benefit">Reduces interior floor fading</li>
        <li class="benefit">Eliminate need for blinds</li>
        <li class="benefit">Strengthen your windows</li>
        <li class="benefit">Insulate in winter</li>
        <li class="benefit">Affoardable</li>
      </ul></li>
    </ul>
  </section>
  <svg class="divider" viewBox="0 0 468 38" preserveAspectRatio="none"><path d="M0 4 H60 Q80 4 95 20 Q108 34 130 34 H338 Q360 34 373 20 Q388 4 408 4 H468" fill="none" stroke="var(--silver)" stroke-width="4"/></svg>
  <section class="contact">
    <p class="cta">CALL BRISBANE’S LEADER IN<br>HOME WINDOW TINTING NOW</p>
    <div class="phones">
      <svg class="phone-icon" viewBox="0 0 36 36"><circle cx="18" cy="18" r="16" fill="none" stroke="var(--gold)" stroke-width="2.5"/><path d="M12 9 l4 0 l1.5 5 l-2.5 2 q2 4 6 6 l2 -2.5 l5 1.5 l0 4 q-1 2 -4 2 q-8 -1 -13 -9 q-2 -5 1 -9z" fill="var(--gold)"/></svg>
      <span class="num">07 3100 4820</span>
      <span class="sms">SMS</span>
      <span class="num">0400 512 736</span>
    </div>
    <p class="web">www.brightpeaktinting.com.au</p>
  </section>
</article>

</body>
</html>
```